BirchLane Hotel
BUSINESS CARDS, LETTERHEAD, ENVELOPES, FAX COVER, EMAIL SIGNATURE, signage, car
BirchLane Hotel - Hospitality Industry
Creative Brief
Simple
DOHYUN KWAK
President & C.E.O
B2 Sora Bldg. 412-5 Mokhwa-dong, Seocho-gu, Seoul, 137-914, Korea
oliver@blhotelgroup.com
www.blhotelgroup.com
BirchLane Pohang: 218-4 Hwajin-dong, Bukgu, Pohang, Korea BirchLane Gunsan: 457 Maeryeong-dong, Gunsan, Korea

```html
<!DOCTYPE html>
<html lang="en">
<head>
<meta charset="utf-8">
<title>BirchLane Hotel — Business Card</title>
<link rel="stylesheet" href="https://fonts.googleapis.com/css2?family=Arimo:wght@400;700&display=swap">
<style>
  :root {
    --backdrop: #d4d5d7;
    --card-white: #ffffff;
    --card-black: #0b0b0b;
    --ink-dark: #111111;
    --ink-light: #ffffff;
    --ink-soft: #c9c9c9;
    --pattern-grey: #4a4a4a;
  }
  * { margin: 0; padding: 0; box-sizing: border-box; }
  html, body {
    width: 1200px;
    height: 850px;
    overflow: hidden;
    background: var(--backdrop);
    font-family: "Arimo", Arial, sans-serif;
  }
  .board { position: relative; width: 1200px; height: 850px; }
  .card {
    position: absolute;
    top: 293px;
    width: 432px;
    height: 240px;
    overflow: hidden;
  }
  .card--front { left: 178px; background: var(--card-black); }
  .card--back { left: 636px; background: var(--card-black); }

  /* front: brand panel */
  .brand-panel {
    position: absolute;
    left: 0; top: 0;
    width: 242px; height: 240px;
    background: var(--card-white);
    display: flex;
    align-items: center;
    justify-content: center;
    gap: 7px;
  }
  .brand-dot {
    width: 12px; height: 12px;
    border-radius: 50%;
    background: var(--ink-dark);
  }
  .brand-name {
    font-size: 17px;
    font-weight: 700;
    color: var(--ink-dark);
    letter-spacing: -0.2px;
  }

  /* decorative pattern areas */
  .pattern {
    position: absolute;
    background: linear-gradient(150deg, #2c2c2c 0%, var(--pattern-grey) 45%, #1a1a1a 100%);
    opacity: 0.75;
  }
  .card--front .pattern--top { left: 300px; top: 0; width: 132px; height: 70px; }
  .card--front .pattern--bottom { left: 330px; top: 190px; width: 102px; height: 50px; }
  .card--back .pattern--field { left: 200px; top: 0; width: 232px; height: 240px; }
  .card--back .pattern--corner { left: 0; top: 0; width: 150px; height: 75px; }
  .card--back .pattern--foot { left: 0; top: 195px; width: 130px; height: 45px; }

  /* front: contact block */
  .contact {
    position: absolute;
    left: 254px;
    top: 66px;
    color: var(--ink-light);
  }
  .contact__name { font-size: 14px; font-weight: 700; letter-spacing: 0.2px; }
  .contact__title { font-size: 8px; margin-top: 2px; color: var(--ink-soft); }
  .contact__lines { margin-top: 11px; font-size: 7px; line-height: 10px; color: var(--ink-soft); }
  .contact__address { margin-top: 7px; font-size: 7px; line-height: 10px; color: var(--ink-soft); }
  .contact__web { margin-top: 11px; font-size: 8px; font-weight: 700; color: var(--ink-light); }

  /* back: locations */
  .locations {
    position: absolute;
    left: 17px;
    top: 108px;
    color: var(--ink-light);
  }
  .location + .location { margin-top: 13px; }
  .location__name { font-size: 8px; font-weight: 700; }
  .location__detail { font-size: 7px; line-height: 10px; color: var(--ink-soft); }
</style>
</head>
<body>
<main class="board">
  <section class="card card--front" aria-label="Business card front">
    <div class="pattern pattern--top" role="img" aria-label="Scattered grey flower and dot pattern"></div>
    <div class="pattern pattern--bottom" role="img" aria-label="Scattered grey flower and dot pattern"></div>
    <div class="brand-panel">
      <span class="brand-dot"></span>
      <span class="brand-name">BirchLane Hotel</span>
    </div>
    <div class="contact">
      <p class="contact__name">DOHYUN KWAK</p>
      <p class="contact__title">President &amp; C.E.O</p>
      <div class="contact__lines">
        <p>tel. 02-555-0142</p>
        <p>fax. 02-555-0143</p>
        <p>cell. 010-555-0178</p>
        <p>email. oliver@blhotelgroup.com</p>
      </div>
      <div class="contact__address">
        <p>B2 Sora Bldg. 412-5 Mokhwa-dong,</p>
        <p>Seocho-gu, Seoul, 137-914, Korea</p>
      </div>
      <p class="contact__web">www.blhotelgroup.com</p>
    </div>
  </section>

  <section class="card card--back" aria-label="Business card back">
    <div class="pattern pattern--field" role="img" aria-label="Scattered grey flower and dot pattern"></div>
    <div class="pattern pattern--corner" role="img" aria-label="Scattered grey flower and dot pattern"></div>
    <div class="pattern pattern--foot" role="img" aria-label="Scattered grey flower and dot pattern"></div>
    <div class="locations">
      <div class="location">
        <p class="location__name">BirchLane Gunsan:</p>
        <p class="location__detail">457 Maeryeong-dong, Gunsan, Korea</p>
        <p class="location__detail">tel. 063-555-0120</p>
      </div>
      <div class="location">
        <p class="location__name">BirchLane Pohang:</p>
        <p class="location__detail">218-4 Hwajin-dong, Bukgu, Pohang, Korea</p>
        <p class="location__detail">tel. 054-555-0131</p>
      </div>
    </div>
  </section>
</main>
</body>
</html>
```